DORLIT HOMES Professional Home Buyers

Please see two files uploaded. One is my new LOGO (thanks Quenby) and the other gives the wording and pages desired. Of course I am open to suggestions to further enhance what I'm about. I don't want testimonials or houses to buy to appear but to have room for them when I'm ready. I am a real estate investor not a licensed real estate agent. For FAQ i want just the questions to appear and when they click on the question the answer appears and when they click on the question again the answer disappears. make sense? When you read my wording and my idea of pages you'll get an idea of what I'm about. Suggestions are welcomed.

Industry/Entity Type

Real Estate

Number of Pages Required

5+ page

Requirements
Must have
• FAQ pages only questions appear. They click on question the answer appears underneath. they click on question again, the answer disappears. Also, I of course, want my new LOGO to appear on each page I don't know if it will look better all by itself or blended in somehow? Call now 418-555-0193 on each page also. I will get a real phone number before website goes live. If you have a better way of wording what I'm describing please let me know, I am open to feedback
Nice to have
• Anything that the average homeowner can relate to (yea I know, that doesn't help you much, right?)
• Testimonial page and houses to buy page could be done with just the shell ready in the wings for when my business grows it will be ready all that it would need then are the wording and pictures to be uploaded onto the website page. make sense?
Should not have
• I don't want it too elegant or rich looking as I believe my audience will be mostly the average homeowner who needs help

```html
<!DOCTYPE html>
<html lang="en">
<head>
<meta charset="utf-8">
<title>DORLIT HOMES – Professional Home Buyers</title>
<link href="https://fonts.googleapis.com/css2?family=Open+Sans:wght@400;600;700;800&display=swap" rel="stylesheet">
<style>
:root{
  --navy:#163f86;
  --blue:#1d55a8;
  --blue-light:#2f6cc2;
  --green:#5aa82a;
  --green-dark:#3f8a18;
  --ink:#333a44;
  --muted:#6b7380;
  --band:#eceef1;
  --line:#d3d7dd;
  --footer:#123574;
  --footer-deep:#0c2757;
  --white:#ffffff;
}
*{box-sizing:border-box;margin:0;padding:0}
html,body{width:1200px;height:2208px;overflow:hidden;background:var(--white)}
body{font-family:"Open Sans",Arial,sans-serif;color:var(--ink)}
.page{width:1200px;height:2208px;position:relative}

/* header */
.site-header{height:124px;display:flex;align-items:center;justify-content:space-between;padding:0 170px 0 160px}
.brand{display:flex;align-items:center;gap:14px}
.brand-mark{width:34px;height:34px;background:var(--navy);border-radius:4px}
.brand-name{font-weight:800;font-size:30px;color:var(--navy);letter-spacing:1px;white-space:nowrap}
.header-call{font-weight:700;font-size:22px;color:var(--navy)}
.header-call span{color:var(--blue-light)}

/* nav */
.main-nav{height:40px;background:var(--blue);display:flex;align-items:center;justify-content:space-between;padding:0 160px 0 150px}
.nav-links{display:flex;list-style:none;height:40px}
.nav-links li{font-size:14px;font-weight:600;color:var(--white);padding:0 16px;line-height:40px}
.nav-links li.active{background:var(--white);color:var(--blue);border-top:3px solid var(--blue-light);line-height:34px}
.social{display:flex;gap:8px}
.social i{width:18px;height:18px;border-radius:50%;background:var(--white);opacity:.85;display:block}

/* hero */
.hero{height:440px;background:linear-gradient(180deg,#5f93d8 0%,#a9c8ea 38%,#d9dde2 60%,#8f9a8a 82%,#4e6b3a 100%)}

/* intro */
.intro{text-align:center;padding:30px 160px 0}
.intro h1{font-size:28px;font-weight:700;color:var(--ink)}
.intro .tagline{font-size:14px;color:var(--blue);margin-top:6px;font-weight:600}
.intro p{font-size:13px;color:var(--muted);line-height:20px;margin:8px auto 0;width:820px}
.btn{display:inline-block;background:var(--green);color:var(--white);font-weight:700;font-size:15px;padding:10px 26px;border-radius:3px;border-bottom:3px solid var(--green-dark)}
.intro .btn{margin-top:18px}

/* reasons */
.reasons{margin-top:32px;height:318px;background:var(--band);display:flex;justify-content:center;gap:60px;padding-top:36px}
.reason{width:280px}
.reason h2{font-size:20px;font-weight:600;color:var(--blue);line-height:26px;height:80px}
.reason ul{list-style:none;margin-top:6px}
.reason li{font-size:13px;color:var(--muted);line-height:30px;display:flex;align-items:center;gap:10px}
.reason li svg{flex:none}
.reason li.hl{color:var(--green)}

/* cash */
.cash{text-align:center;padding:42px 0 0}
.cash h2{font-size:24px;font-weight:600;color:var(--blue)}
.cash p{font-size:13px;color:var(--muted);line-height:20px;width:860px;margin:10px auto 0}
.cash .btn{margin-top:26px;font-size:14px;padding:9px 26px}

/* call banner */
.call-banner{margin:44px auto 0;width:880px;height:92px;background:var(--blue);border-radius:4px;display:flex;align-items:center;padding:0 36px;gap:28px;box-shadow:0 3px 0 var(--navy);white-space:nowrap;overflow:hidden}
.call-banner strong{font-size:38px;font-weight:400;color:var(--white);letter-spacing:1px}
.call-banner span{font-size:17px;color:var(--white);line-height:24px;opacity:.95}

/* inquiry */
.inquiry{margin-top:44px;background:var(--band);height:410px;padding-top:24px}
.inquiry h2{text-align:center;font-size:26px;font-weight:400;color:var(--ink)}
.inquiry-form{width:880px;margin:22px auto 0;display:grid;grid-template-columns:repeat(3,1fr);gap:16px 24px}
.field{height:34px;background:var(--white);border:1px solid var(--line);font-size:12px;color:#9aa1ab;padding:8px 10px}
.inquiry .btn{display:block;width:130px;margin:22px auto 0;text-align:center;font-size:14px;padding:9px 0}

/* footer */
.site-footer{position:absolute;top:1912px;left:0;width:1200px;height:264px;background:var(--footer);display:flex;padding:40px 0 0 168px;gap:56px;color:#c9d4ea}
.site-footer h3{font-size:17px;font-weight:600;color:var(--white);margin-bottom:12px}
.site-footer ul{list-style:none}
.site-footer li{font-size:12px;line-height:22px}
.foot-col{width:150px}
.foot-address{width:260px}
.foot-address li{display:flex;gap:10px;align-items:flex-start;margin-bottom:6px}
.foot-address li svg{flex:none;margin-top:4px}
.foot-brand{margin-left:20px;display:flex;flex-direction:column;align-items:center;gap:10px;padding-top:28px}
.foot-brand .brand-mark{width:40px;height:40px;background:var(--white);opacity:.8}
.foot-brand .brand-name{color:var(--white);font-size:28px}
.bottom-bar{position:absolute;top:2176px;left:0;width:1200px;height:32px;background:var(--footer-deep);display:flex;align-items:center;justify-content:space-between;padding:0 170px;font-size:11px;color:#9fb0cf}
.bottom-bar .social i{width:14px;height:14px;opacity:.6}
</style>
</head>
<body>
<div class="page">

  <header class="site-header">
    <div class="brand"><span class="brand-mark"></span><span class="brand-name">DORLIT HOMES</span></div>
    <div class="header-call">CALL NOW: <span>418-555-0193</span></div>
  </header>

  <nav class="main-nav">
    <ul class="nav-links">
      <li class="active">HOME</li><li>ABOUT US</li><li>TESTIMONIALS</li><li>HOUSES TO BUY</li><li>FAQ</li><li>CONTACT US</li>
    </ul>
    <div class="social"><i></i><i></i><i></i></div>
  </nav>

  <div class="hero" role="img" aria-label="Photo of a two-storey suburban house with a lawn under a blue sky"></div>

  <section class="intro">
    <h1>We buy houses in any condition!</h1>
    <div class="tagline">DORLIT HOMES will buy your house AS IS · FAST and · HASSLE FREE!</div>
    <p>Don't waste another penny on expensive repairs! DORLIT HOMES is currently buying houses throughout the area. We buy houses "as is", we pay cash, we handle all traditional closing costs and we can close in as quickly as a week. Contact us today for your free, no obligation quote.</p>
    <span class="btn">GET YOUR FREE QUOTE</span>
  </section>

  <section class="reasons">
    <div class="reason">
      <h2>Sell your home<br>FAST!</h2>
      <ul>
        <li><svg width="12" height="12" viewBox="0 0 12 12"><path d="M1 6l3.5 3.5L11 2" stroke="#5aa82a" stroke-width="2" fill="none"/></svg>We pay all cash</li>
        <li class="hl"><svg width="12" height="12" viewBox="0 0 12 12"><path d="M1 6l3.5 3.5L11 2" stroke="#5aa82a" stroke-width="2" fill="none"/></svg>We pay closing costs</li>
        <li><svg width="12" height="12" viewBox="0 0 12 12"><path d="M1 6l3.5 3.5L11 2" stroke="#5aa82a" stroke-width="2" fill="none"/></svg>We buy "as is"</li>
        <li><svg width="12" height="12" viewBox="0 0 12 12"><path d="M1 6l3.5 3.5L11 2" stroke="#5aa82a" stroke-width="2" fill="none"/></svg>No waiting for bank loan approvals</li>
        <li><svg width="12" height="12" viewBox="0 0 12 12"><path d="M1 6l3.5 3.5L11 2" stroke="#5aa82a" stroke-width="2" fill="none"/></svg>Quick closings</li>
      </ul>
    </div>
    <div class="reason">
      <h2>Why sell to DORLIT HOMES?</h2>
      <ul>
        <li><svg width="12" height="12" viewBox="0 0 12 12"><path d="M1 6l3.5 3.5L11 2" stroke="#5aa82a" stroke-width="2" fill="none"/></svg>We pay all cash</li>
        <li><svg width="12" height="12" viewBox="0 0 12 12"><path d="M1 6l3.5 3.5L11 2" stroke="#5aa82a" stroke-width="2" fill="none"/></svg>We pay most closing costs</li>
        <li><svg width="12" height="12" viewBox="0 0 12 12"><path d="M1 6l3.5 3.5L11 2" stroke="#5aa82a" stroke-width="2" fill="none"/></svg>We buy "as is"</li>
        <li><svg width="12" height="12" viewBox="0 0 12 12"><path d="M1 6l3.5 3.5L11 2" stroke="#5aa82a" stroke-width="2" fill="none"/></svg>We charge no fees</li>
        <li><svg width="12" height="12" viewBox="0 0 12 12"><path d="M1 6l3.5 3.5L11 2" stroke="#5aa82a" stroke-width="2" fill="none"/></svg>We close quickly</li>
      </ul>
    </div>
    <div class="reason">
      <h2>People sell their houses to DORLIT HOMES for a variety of reasons</h2>
      <ul>
        <li><svg width="12" height="12" viewBox="0 0 12 12"><path d="M1 6l3.5 3.5L11 2" stroke="#5aa82a" stroke-width="2" fill="none"/></svg>To avoid foreclosure</li>
        <li><svg width="12" height="12" viewBox="0 0 12 12"><path d="M1 6l3.5 3.5L11 2" stroke="#5aa82a" stroke-width="2" fill="none"/></svg>Facing a death or divorce</li>
        <li><svg width="12" height="12" viewBox="0 0 12 12"><path d="M1 6l3.5 3.5L11 2" stroke="#5aa82a" stroke-width="2" fill="none"/></svg>A job transfer or relocation</li>
        <li><svg width="12" height="12" viewBox="0 0 12 12"><path d="M1 6l3.5 3.5L11 2" stroke="#5aa82a" stroke-width="2" fill="none"/></svg>Inheriting property</li>
        <li><svg width="12" height="12" viewBox="0 0 12 12"><path d="M1 6l3.5 3.5L11 2" stroke="#5aa82a" stroke-width="2" fill="none"/></svg>Downsizing or retiring</li>
      </ul>
    </div>
  </section>

  <section class="cash">
    <h2>Get cash for your house!</h2>
    <p><strong>DORLIT HOMES</strong> has real estate investors ready to buy your house in as little as seven days. We buy houses, townhouses, condos, duplexes and multi-tenant buildings from owners looking to sell quickly!</p>
    <span class="btn">READ MORE</span>
  </section>

  <div class="call-banner">
    <strong>CALL NOW: 418-555-0193</strong>
    <span>We want to hear from you!<br>Call DORLIT HOMES today or fill out form</span>
  </div>

  <section class="inquiry">
    <h2>Quick Inquiry</h2>
    <div class="inquiry-form">
      <div class="field">First Name</div><div class="field">Last Name</div><div class="field">Phone</div>
      <div class="field">Address</div><div class="field">Email</div><div class="field">City</div>
      <div class="field">Street address</div><div class="field">Unit</div><div class="field">Condition</div>
      <div class="field">State</div><div class="field">Zip</div><div class="field">Contact with Number</div>
    </div>
    <span class="btn">SUBMIT</span>
  </section>

  <footer class="site-footer">
    <div class="foot-col">
      <h3>Quick Links</h3>
      <ul><li>Home</li><li>About Us</li><li>Testimonials</li><li>Houses to Buy</li><li>FAQ</li><li>Contact Us</li></ul>
    </div>
    <div class="foot-col">
      <h3>Support Menu</h3>
      <ul><li>Lost Password?</li><li>Forgot your Username?</li><li>Your Membership</li><li>Your Account</li><li>Support Forum</li><li>Privacy</li></ul>
    </div>
    <div class="foot-address">
      <h3>Address</h3>
      <ul>
        <li><svg width="10" height="14" viewBox="0 0 10 14"><path d="M5 0a5 5 0 0 0-5 5c0 4 5 9 5 9s5-5 5-9a5 5 0 0 0-5-5z" fill="#c9d4ea"/></svg>Call or write anytime and we will reply within one business day</li>
        <li><svg width="12" height="12" viewBox="0 0 12 12"><path d="M2 1l2 0 1 3-1.5 1a7 7 0 0 0 3.5 3.5L8 7l3 1v2a1 1 0 0 1-1 1A9 9 0 0 1 1 2a1 1 0 0 1 1-1z" fill="#c9d4ea"/></svg>418-555-0193</li>
        <li><svg width="12" height="12" viewBox="0 0 12 12"><path d="M2 1l2 0 1 3-1.5 1a7 7 0 0 0 3.5 3.5L8 7l3 1v2a1 1 0 0 1-1 1A9 9 0 0 1 1 2a1 1 0 0 1 1-1z" fill="#c9d4ea"/></svg>418-555-0193</li>
        <li><svg width="12" height="10" viewBox="0 0 12 10"><rect x="0.5" y="0.5" width="11" height="9" fill="none" stroke="#c9d4ea"/><path d="M1 1l5 4 5-4" fill="none" stroke="#c9d4ea"/></svg>hello@dorlithomes.com</li>
      </ul>
    </div>
    <div class="foot-brand"><span class="brand-mark"></span><span class="brand-name">DORLIT HOMES</span></div>
  </footer>
  <div class="bottom-bar"><span>© 2024 DORLIT HOMES</span><div class="social"><i></i><i></i><i></i></div></div>

</div>
</body>
</html>
```